Footprints and name in the sand

I need a Photoshop design of a parents' and baby/toddler footprints in sand on the beach. Above the footprints written in the sand is the name Tilly Brannock 11th May 2022 7lb 2oz, the details can be on separate lines. There can be shells and starfish on the sand. The format size of the image can either be A4/A3 etc., paper size or 1:1 square. The picture can be photo-realistic or cartoon - I think I may prefer photo-realistic but I won't know until I see the designs. I'll be printing at A2 or 20" x 20" size.
I have attached my pathetic attempts at doing this so you can see what NOT to do.
What I don't like about my designs:
1) The effect on the letters doesn't match the effect on the feet.
2) Neither effects are very good.
3) As something that is going to be framed and hung on a wall it isn't really an attractive piece.
4) It is neither photo-realistic or cartoon
What I do like is the sea and the shell.

Finally the text needs to editable so I will need an accompanying PS action with the design.

```html
<!DOCTYPE html>
<html lang="en">
<head>
<meta charset="utf-8">
<title>Tilly Brannock – Footprints in the Sand</title>
<link rel="stylesheet" href="https://fonts.googleapis.com/css2?family=Comic+Neue:wght@700&display=swap">
<style>
  :root {
    --sand-light: #f8dfc4;
    --sand-mid: #f3d4b4;
    --sand-deep: #e9c9a2;
    --groove: #dcbd8f;
    --groove-shadow: rgba(135, 95, 50, 0.6);
    --groove-light: rgba(255, 247, 232, 0.95);
    --print-fill: #e4c598;
    --star-fill: #e2c294;
    --sea-deep: #58c4c0;
    --sea-mid: #86d8cf;
    --sea-shallow: #bfe6d6;
    --foam: #fbfaf4;
  }
  html, body {
    margin: 0;
    padding: 0;
    overflow: hidden;
    background: #ffffff;
  }
  .poster {
    position: relative;
    width: 850px;
    height: 1200px;
    overflow: hidden;
    background: linear-gradient(180deg, var(--sand-mid) 0%, var(--sand-light) 50%, var(--sand-mid) 100%);
  }
  .sea {
    position: absolute;
    left: 0;
    top: 0;
    width: 850px;
    height: 560px;
  }
  .sand-writing {
    position: absolute;
    margin: 0;
    font-family: "Comic Neue", cursive;
    font-weight: 700;
    color: var(--groove);
    line-height: 1;
    white-space: nowrap;
    text-shadow:
      -2px -2px 0 var(--groove-shadow),
      3px 3px 0 var(--groove-light),
      4px 4px 6px rgba(255, 238, 210, 0.9);
  }
  .first-name {
    left: 194px;
    top: 488px;
    font-size: 140px;
  }
  .surname {
    left: 52px;
    top: 624px;
    font-size: 140px;
  }
  .birth-date {
    left: 149px;
    top: 772px;
    font-size: 100px;
    letter-spacing: 2px;
  }
  .birth-weight {
    left: 678px;
    top: 800px;
    font-size: 40px;
    transform: rotate(20deg);
    transform-origin: left center;
  }
  .footprints {
    position: absolute;
    left: 128px;
    top: 968px;
    width: 486px;
    height: 192px;
    border-radius: 18px;
    background: var(--print-fill);
  }
  .starfish {
    position: absolute;
    left: 672px;
    top: 1030px;
    width: 126px;
    height: 120px;
    border-radius: 14px;
    background: var(--star-fill);
  }
</style>
</head>
<body>
  <main class="poster">
    <svg class="sea" viewBox="0 0 850 560" role="img" aria-label="Aerial photo of clear turquoise sea washing onto the sand with a white foamy wave edge">
      <defs>
        <linearGradient id="water" x1="0" y1="0" x2="0" y2="1">
          <stop offset="0" stop-color="var(--sea-deep)"/>
          <stop offset="0.6" stop-color="var(--sea-mid)"/>
          <stop offset="1" stop-color="var(--sea-shallow)"/>
        </linearGradient>
      </defs>
      <path d="M0 0 H850 V445 C770 468 700 478 610 476 C490 474 380 470 260 486 C160 500 70 526 0 550 Z" fill="var(--foam)"/>
      <path d="M0 0 H850 V395 C770 425 690 438 600 438 C480 438 370 430 250 446 C150 460 70 488 0 512 Z" fill="url(#water)"/>
    </svg>

    <h1 class="sand-writing first-name">Tilly</h1>
    <p class="sand-writing surname">Brannock</p>
    <p class="sand-writing birth-date">11-05-22</p>
    <p class="sand-writing birth-weight">7lb 2oz</p>

    <div class="footprints" role="img" aria-label="Two pairs of parents' footprints pressed into the sand with a small pair of baby footprints between them"></div>
    <div class="starfish" role="img" aria-label="Sandy starfish lying on the beach"></div>
  </main>
</body>
</html>
```